National Training and assessment company needs a website

Create a 4 page website, simple but professional, the company provides training services to industry, resumes'/ CVs, personnel skill assessment, workplace skills profiling and develops manufactures and supplies training equipment for electrical/engineering training, Company title is Toren K Pty Ltd and also trades under BRW & Associates. letterheads etc all are done using dark green
Reason: Due to work commitments will be interstate from the 26/02 til 05/03/14
Target Market(s)
The market is broad covering the general public, secondary colleges and corporate sector
Industry/Entity Type
Training
Look and feel

```html
<!DOCTYPE html>
<html lang="en">
<head>
<meta charset="utf-8">
<title>BRW &amp; Associates – Toren K Pty Ltd</title>
<link href="https://fonts.googleapis.com/css2?family=Marcellus&family=Arimo:wght@400;700&display=swap" rel="stylesheet">
<style>
:root{
  --green:#3f9a44;
  --green-text:#3a9a3f;
  --cream:#f0eed9;
  --cream-btn:#ebe9cc;
  --white:#ffffff;
  --body-text:#555555;
  --dark:#222222;
  --footer-text:#f4f4ea;
}
*{box-sizing:border-box;margin:0;padding:0}
html,body{width:1057px;height:1200px;overflow:hidden}
body{position:relative;background:var(--white);font-family:"Arimo",Arial,sans-serif;color:var(--body-text)}
.serif{font-family:"Marcellus",Georgia,serif}

/* header */
.site-header{position:absolute;left:0;top:0;width:1057px;height:48px;background:var(--cream);box-shadow:0 2px 4px rgba(0,0,0,.25);z-index:2}
.brand{position:absolute;left:138px;top:9px;font-family:"Marcellus",Georgia,serif;font-size:24px;color:var(--green-text)}
.main-nav{position:absolute;left:405px;top:17px;display:flex;gap:34px;font-size:12.5px}
.main-nav a{color:var(--dark);text-decoration:none}
.main-nav a.active{color:var(--green-text)}
.header-phone{position:absolute;left:784px;top:12px;display:flex;align-items:center;gap:8px;font-family:"Marcellus",Georgia,serif;font-size:20px;color:var(--green-text);font-weight:700}

/* hero */
.hero{position:absolute;left:0;top:48px;width:1057px;height:494px;background:radial-gradient(ellipse at center,#46a34a 0%,var(--green) 60%,#3a9340 100%)}
.hero-title{position:absolute;left:0;width:1057px;top:46px;text-align:center;font-size:30px;line-height:36px;color:#f4f1dc;font-weight:400}
.hero-art{position:absolute;left:130px;top:120px;width:797px;height:350px;border-radius:12px;background:radial-gradient(ellipse at center,rgba(240,238,217,.22) 0%,rgba(240,238,217,.08) 55%,rgba(240,238,217,0) 80%)}
.hero-arrow{position:absolute;top:230px}
.hero-arrow.prev{left:118px}
.hero-arrow.next{left:920px}

/* sections */
.section-title{font-family:"Marcellus",Georgia,serif;color:var(--green-text);font-size:25px;letter-spacing:.5px;font-weight:400}
.copy{font-size:11.3px;line-height:13.6px;letter-spacing:.2px}
.about{position:absolute;left:138px;top:586px;width:497px}
.about .copy{margin-top:24px;text-align:justify}
.about .copy+.copy{margin-top:13px}
.btn{display:inline-block;margin-top:16px;width:116px;height:28px;line-height:29px;text-align:center;background:var(--cream-btn);border-radius:3px;font-family:"Marcellus",Georgia,serif;font-size:14px;color:var(--green-text);font-weight:700;text-decoration:none}
.divider{position:absolute;left:652px;width:20px;background:linear-gradient(90deg,rgba(0,0,0,.06),rgba(0,0,0,0))}
.services{position:absolute;left:679px;top:586px;width:290px}
.services .copy{margin-top:24px;padding-left:2px;width:234px}
.service-list{list-style:none;margin-top:28px}
.service-list li{display:flex;align-items:center;gap:8px;font-size:11px;color:var(--green-text);height:24.5px;white-space:nowrap}

.lower{position:absolute;left:0;top:883px;width:1057px;height:273px;background:var(--cream)}
.about-me{position:absolute;left:138px;top:32px;width:497px}
.about-me .section-title{font-size:21px}
.portrait{position:absolute;left:1px;top:52px;width:145px;height:145px;border:1px solid #555;background:var(--white);box-shadow:0 8px 8px -4px rgba(0,0,0,.3)}
.portrait-fill{position:absolute;left:5px;top:5px;width:133px;height:133px;background:radial-gradient(circle at 50% 40%,#8fcf8b,#3f9a44 75%)}
.bio{position:absolute;left:160px;top:50px;width:337px}
.bio-name{font-family:"Marcellus",Georgia,serif;font-size:15px;color:var(--green-text);font-weight:700}
.bio-role{font-family:"Marcellus",Georgia,serif;font-size:11px;font-style:italic;color:var(--dark)}
.bio .copy{margin-top:20px;text-align:justify}
.bio a{color:var(--green-text);text-decoration:none}
.contact{position:absolute;left:679px;top:32px;width:250px}
.contact .section-title{font-size:21px}
.contact-row{display:flex;gap:9px;font-size:11.3px;line-height:13.6px;margin-top:12px}
.contact-row:first-of-type{margin-top:28px}
.contact-row svg{flex:none;margin-top:2px}

/* footer */
.site-footer{position:absolute;left:0;top:1156px;width:1057px;height:44px;background:var(--green);border-top:2px solid #6a6a6a}
.footer-nav{position:absolute;left:140px;top:15px;font-size:10px;color:var(--footer-text)}
.footer-nav a{color:var(--footer-text);text-decoration:none}
.copyright{position:absolute;left:644px;top:15px;font-size:10px;color:var(--footer-text)}
.social{position:absolute;left:830px;top:8px;display:flex;gap:7px}
.social span{width:25px;height:25px;border-radius:50%;background:#e9e8d6}
</style>
</head>
<body>
<header class="site-header">
  <div class="brand">BRW &amp; Associates</div>
  <nav class="main-nav">
    <a class="active" href="#">Home</a>
    <a href="#">About us</a>
    <a href="#">Products &amp; Services</a>
    <a href="#">Contact us</a>
  </nav>
  <div class="header-phone">
    <svg width="20" height="24" viewBox="0 0 20 24"><path d="M4 1 L8 1 L9 7 L6 9 Q8 15 12 18 L15 16 L19 18 L18 22 Q16 24 12 22 Q3 16 2 6 Q2 2 4 1Z" fill="#222"/></svg>
    <span>03 5550 1842</span>
  </div>
</header>

<section class="hero">
  <h1 class="hero-title serif">Toren K Pty Ltd is dedicated to providing quality<br>customer focused service in all its ventures</h1>
  <div class="hero-art" role="img" aria-label="Silhouettes of business people standing on white jigsaw puzzle pieces"></div>
  <svg class="hero-arrow prev" width="22" height="40" viewBox="0 0 22 40"><path d="M20 2 L2 20 L20 38" fill="none" stroke="#f4f1dc" stroke-width="1.5"/></svg>
  <svg class="hero-arrow next" width="22" height="40" viewBox="0 0 22 40"><path d="M2 2 L20 20 L2 38" fill="none" stroke="#f4f1dc" stroke-width="1.5"/></svg>
</section>

<section class="about">
  <h2 class="section-title">ABOUT US</h2>
  <p class="copy">The business was established in 1996 trading as BRW &amp; Associates and registered as a company (Toren K) in 2002. Over this time Toren K trading as BRW &amp; Associates has built a client base Australia wide aligning engineering trades people against the National training agenda therefore enhancing their employment/career opportunities. The company has built a client base of Ex serving defence force engineering members assisting to align military skills to the industrial sector. This has extended to the general engineering public keen to update qualifications and align to the National training agenda in competency terms.</p>
  <p class="copy">Toren K also provides training equipment, curriculum development and advice to the education sector.</p>
  <a class="btn" href="#">Read More</a>
</section>

<div class="divider" style="top:575px;height:260px"></div>

<section class="services">
  <h2 class="section-title">OUR SERVICES</h2>
  <p class="copy">Toren K Pty Ltd is dedicated to providing quality customer focused service in all its ventures. Toren K core business is workplace training assessment with broader services which include:</p>
  <ul class="service-list">
    <li><svg width="10" height="12" viewBox="0 0 10 12"><path d="M1 1 L8 6 L1 11" fill="none" stroke="#3a9a3f" stroke-width="3"/></svg>Employer Workplace skills profiling</li>
    <li><svg width="10" height="12" viewBox="0 0 10 12"><path d="M1 1 L8 6 L1 11" fill="none" stroke="#3a9a3f" stroke-width="3"/></svg>Employee skills profiling (Competency Profiling)</li>
    <li><svg width="10" height="12" viewBox="0 0 10 12"><path d="M1 1 L8 6 L1 11" fill="none" stroke="#3a9a3f" stroke-width="3"/></svg>Workplace training and Assessment</li>
    <li><svg width="10" height="12" viewBox="0 0 10 12"><path d="M1 1 L8 6 L1 11" fill="none" stroke="#3a9a3f" stroke-width="3"/></svg>Resume and Curricula Vita compilation</li>
  </ul>
</section>

<section class="lower">
  <div class="divider" style="top:20px;height:200px"></div>
  <div class="about-me">
    <h2 class="section-title">ABOUT ME</h2>
    <div class="portrait"><div class="portrait-fill" role="img" aria-label="Portrait photo of the company director"></div></div>
    <div class="bio">
      <div class="bio-name">Daniel Hartley</div>
      <div class="bio-role">Director of Toren K</div>
      <p class="copy">Daniel has many years' experience in training and assessment and has a trade back ground as an electrical fitter/mechanic gained whilst a member of the armed services. After a long career in the service he has spent several years managing &amp; delivering for the military, industry, Tafe, private registered training organisations and lectured in Mechatronics Engineering in University and Tafe. <a href="#">Read More [...]</a></p>
    </div>
  </div>
  <div class="contact">
    <h2 class="section-title">CONTACT US</h2>
    <div class="contact-row">
      <svg width="20" height="14" viewBox="0 0 20 14"><rect x="0" y="0" width="20" height="14" rx="2" fill="#222"/><path d="M2 2 L10 8 L18 2 M2 12 L7 7 M18 12 L13 7" fill="none" stroke="#f0eed9" stroke-width="1.5"/></svg>
      <div>Toren K Pty Ltd<br>P.O. Box 2281<br>Larkmont Heights<br>Victoria<br>3999</div>
    </div>
    <div class="contact-row">
      <svg width="20" height="14" viewBox="0 0 20 14"><path d="M1 5 Q10 -2 19 5 L16 7 L14 4 L6 4 L4 7Z" fill="#222"/><rect x="4" y="7" width="12" height="7" rx="2" fill="#222"/><circle cx="10" cy="10" r="2" fill="#f0eed9"/></svg>
      <div>0400 555 218</div>
    </div>
    <div class="contact-row">
      <svg width="20" height="14" viewBox="0 0 22 14"><rect x="0" y="4" width="22" height="10" rx="2" fill="#222"/><rect x="5" y="0" width="12" height="6" fill="#222"/><rect x="7" y="2" width="8" height="3" fill="#f0eed9"/></svg>
      <div>0400 555 218</div>
    </div>
  </div>
</section>

<footer class="site-footer">
  <nav class="footer-nav"><a href="#">Home</a> | &nbsp;<a href="#">About us</a> | &nbsp;<a href="#">Products &amp; Services</a> | &nbsp;<a href="#">Contact us</a></nav>
  <div class="copyright">Copyright © 2014 BRW &amp; ASSOCIATES</div>
  <div class="social"><span></span><span></span><span></span></div>
</footer>
</body>
</html>
```